Plakat-Design für ein Studierendenwerk
Zielgruppe
Wer wir sind:
Das Studierendenwerk Mirabach betreut im Auftrag des Landes Baden-Württemberg in Karlsruhe und Pforzheim circa 48.000 Studierende in allen Fragen rund um das Studium. Bei uns sind alle Studierenden richtig, wenn Sie...
- BAföG beantragen wollen oder Beratung bei der Studienfinanzierung brauchen,
- Einen Platz im Studentenwohnheim suchen,
- in Mensen und Cafeterien essen wollen,
- rechtliche Probleme haben (Erstberatung),
- ein Studienabschlussdarlehen benötigen,
- einen Platz in einer Kinderbetreuungseinrichtung benötigen,
- an studentischer Kultur interessiert sind,
- kostenlose psychotherapeutische Beratung suchen.
www.sw-mr.de
Unsere Zielgruppe:
Unsere Zielgruppe sind primär Studierende im Alter von 20 - 30 Jahren, überwiegend männlich.
Aufgabenstellung
Plakatgröße: DIN A 1
Thema: Osteraktion in unseren Cafeterien
Hintergrundinfo: Es gibt besonders günstige Rüblischnitten zum Einkaufspreis (siehe Beispielbilddatei). Der Kuchen kostet nur 1,30 € pro Stück für den Kunden.
Das MUSS aufs Plakat:
- Bitte Verwendung unserer Plakatvorlage.
- Bitte Einhaltung unserer CI.
- Angabe Aktionszeitraum: 15. - 18.04.19
Gestaltung:
Abbildung nicht zwingend notwendig. Österliches Thema/Motiv (Osterhase?!). Symbolisch/grafisch das Thema Ostern aufgreifen. Gerne auch eigene Ideen gewünscht.

```html
<!DOCTYPE html>
<html lang="de">
<head>
<meta charset="utf-8">
<title>Osteraktion – Studierendenwerk Mirabach</title>
<link rel="stylesheet" href="https://fonts.googleapis.com/css2?family=Titan+One&family=Open+Sans:wght@600;700&display=swap">
<style>
  :root {
    --header: #1f8fc8;
    --accent: #ffec00;
    --ink: #041619;
    --type-blue: #4a84c4;
    --date-blue: #1aa0d8;
    --url-grey: #9a9a9a;
  }
  * { margin: 0; padding: 0; box-sizing: border-box; }
  html, body { width: 849px; height: 1200px; overflow: hidden; background: #fff; }
  .poster {
    position: relative;
    width: 849px;
    height: 1200px;
    overflow: hidden;
    font-family: "Open Sans", Arial, sans-serif;
  }
  .header-band {
    position: absolute; left: 0; top: 0; width: 849px; height: 175px;
    background: var(--header);
    display: flex; align-items: center; justify-content: center;
  }
  .brand-name {
    color: #fff; font-weight: 700; font-size: 26px; letter-spacing: 0.5px;
  }
  .scene {
    position: absolute; left: 0; top: 175px; width: 849px; height: 959px;
    background:
      radial-gradient(circle at 8% 12%, #ffffff 0%, rgba(255,255,240,0.9) 14%, rgba(255,255,200,0) 40%),
      linear-gradient(180deg, #e4e35a 0%, #eeee88 45%, #e8ec94 70%, #9cc84a 88%, #6fa62a 100%);
  }
  .cake-photo {
    position: absolute; left: 152px; top: 402px; width: 530px; height: 356px;
    border-radius: 60px;
    background: radial-gradient(ellipse at 55% 45%, #b8834a 0%, #d9b37a 40%, #f1f1f3 62%, #e6e8ee 100%);
  }
  .headline {
    position: absolute; left: 0; top: 236px; width: 849px; text-align: center;
    font-family: "Titan One", "Arial Black", sans-serif;
    font-style: italic; font-size: 92px; line-height: 1; font-weight: 400;
    background: linear-gradient(180deg, #0aa3d8 0%, #4f86c8 100%);
    -webkit-background-clip: text; background-clip: text; color: transparent;
    filter: drop-shadow(3px 4px 3px rgba(60,60,20,0.55));
  }
  .period {
    position: absolute; left: 274px; top: 322px;
    font-weight: 600; font-size: 44px; line-height: 1; color: var(--date-blue);
  }
  .offer {
    position: absolute; left: 424px; top: 778px; color: var(--type-blue);
    font-weight: 600; text-transform: uppercase;
  }
  .offer-title { font-weight: 700; font-size: 41px; line-height: 1; letter-spacing: 0.5px; }
  .offer-line { font-size: 28px; line-height: 1; margin-top: 14px; }
  .offer-price { font-size: 44px; font-weight: 700; }
  .accent-line {
    position: absolute; left: 0; top: 1134px; width: 849px; height: 6px;
    background: var(--accent);
  }
  .footer {
    position: absolute; left: 0; top: 1140px; width: 849px; height: 60px;
    background: var(--ink);
    display: flex; align-items: center; justify-content: center;
    color: var(--url-grey); font-weight: 700; font-size: 22px; letter-spacing: 0.5px;
  }
</style>
</head>
<body>
<div class="poster">
  <header class="header-band">
    <p class="brand-name">Studierendenwerk Mirabach</p>
  </header>

  <div class="scene" role="img" aria-label="Sonnige gelbgrüne Frühlingswiese, aus dem Gras ragen die Ohren eines Osterhasen"></div>
  <div class="cake-photo" role="img" aria-label="Foto: Stück Rüblikuchen mit Puderzucker und Marzipankarotte auf weißem Teller"></div>

  <h1 class="headline">OSTERAKTION</h1>
  <p class="period">15. - 18.04.19</p>

  <div class="offer">
    <p class="offer-title">Rüblischnitten</p>
    <p class="offer-line">zum Einkaufspreis</p>
    <p class="offer-line">nur <span class="offer-price">1,30 €</span> pro Stück</p>
  </div>

  <div class="accent-line"></div>
  <footer class="footer">www.sw-mr.de</footer>
</div>
</body>
</html>
```